Free Printer Promotion

Hi i need a banner AD for my website.

The promotion is: free printer, for a monthly cost you get all the supplies and service included. Its a subscription service for printing. There is 5 plans available.
Prices vary upon printers, most expensive plan is $69.94 a month for a 1 year term and the most affordable plan is $9.95 a month for 3 year term

1 Monochrome laser (print only printer, black and white printing)
2 Multifunction Monochrome laser (print scan copy fax printer, black and white printing)

• Monochrome Printers are given 1000 prints per month
• Toner included
• Service included
• Printer included

3 Color laser (print only printer, color printing)
4 Multifunction Color laser (print scan copy fax, color printing)
Color printers are given 500 monochrome prints and 500 color prints per month
• Toner included
• Service included
• Printer included

5 Inkjet color printer (print copy scan fax, color printing)
• Inkjet Printers are given 1000 prints per month.
• Ink included
• Service included
• Printer included

Target Market(s)

students, home office workers, corporate business and government

Font styles to use
Serif
Sans Serif

Requirements
Must have
• i want it to be enticing, no long sentences. the customer will click on the banner and it will bring them to another page with the information.

Keep it short and sweet.

```html
<!DOCTYPE html>
<html lang="en">
<head>
<meta charset="utf-8">
<title>Free Printer Promotion – Banner and Full Ad</title>
<link rel="stylesheet" href="https://fonts.googleapis.com/css2?family=Anton&family=Roboto:wght@400;500&family=Roboto+Condensed:wght@400;500&display=swap">
<style>
:root{
  --navy-stage:#001240;
  --black-stage:#0b0b0b;
  --ink-navy:#0c1c52;
  --badge-navy:#0a1845;
  --teal:#03668f;
  --teal-dark:#0a3f55;
  --teal-text:#0a6891;
  --pale-box:#e3eef1;
  --text-dark:#16213a;
  --free-gray:#333438;
  --white:#ffffff;
}
*{margin:0;padding:0;box-sizing:border-box}
html,body{width:960px;height:1200px;overflow:hidden}
body{position:relative;font-family:"Roboto",Arial,sans-serif;background:var(--black-stage)}
.stage-top{position:absolute;left:0;top:0;width:960px;height:409px;background:var(--navy-stage)}
.stage-bottom{position:absolute;left:0;top:409px;width:960px;height:791px;background:var(--black-stage)}
.stage-label{position:absolute;color:var(--white);font-size:20px;font-weight:400;line-height:1}

/* Banner */
.banner{position:absolute;left:96px;top:108px;width:768px;height:192px;overflow:hidden;
  background:linear-gradient(180deg,#2c5c9a 0%,#3a86d4 55%,#43a1f6 100%)}
.banner-photo{position:absolute;left:0;top:0}
.badge{position:absolute}
.badge-text{position:absolute;inset:0;display:flex;flex-direction:column;align-items:center;justify-content:center;color:var(--white);text-align:center}
.banner .badge{left:21px;top:8px;width:122px;height:122px}
.banner .badge-price{font-size:24px;font-weight:500;line-height:26px}
.banner .badge-line{font-size:15px;line-height:19px}
.banner-title{position:absolute;left:440px;width:316px;top:18px;text-align:center;font-family:"Anton",Impact,sans-serif;
  font-size:44px;line-height:54px;color:var(--white);letter-spacing:.5px;text-shadow:2px 2px 3px rgba(0,0,0,.45)}
.banner-sub{position:absolute;left:436px;width:324px;top:74px;text-align:center;font-size:18.5px;line-height:23px;color:var(--ink-navy)}
.banner-cta{position:absolute;left:458px;top:131px;width:276px;height:38px;border-radius:19px;background:var(--ink-navy);
  box-shadow:0 4px 6px rgba(0,0,0,.4);display:flex;align-items:center;justify-content:center;gap:14px;
  font-family:"Anton",Impact,sans-serif;font-size:25px;color:var(--white);letter-spacing:.3px}

/* Full ad */
.full-ad{position:absolute;left:279px;top:473px;width:364px;height:727px;background:var(--white);overflow:hidden;
  box-shadow:0 0 30px rgba(0,0,0,.6)}
.ad-header{position:absolute;left:0;top:0;width:364px;height:150px;background:linear-gradient(180deg,#ffffff 0%,#f1f5f8 55%,#dbe6ee 100%)}
.ad-photo{position:absolute;left:0;top:0}
.ad-title{position:absolute;left:175px;top:30px;font-family:"Anton",Impact,sans-serif;font-size:43px;line-height:40px;letter-spacing:.3px}
.ad-title .free{color:var(--free-gray);display:block}
.ad-title .printer{color:var(--teal-text);display:block}
.full-ad .badge{left:281px;top:9px;width:74px;height:74px}
.full-ad .badge-price{font-size:14px;font-weight:500;line-height:15px}
.full-ad .badge-line{font-size:8.5px;line-height:11px}
.ad-sub{position:absolute;left:175px;top:112px;font-size:12.5px;line-height:14px;color:var(--text-dark)}
.plans-band{position:absolute;left:0;top:150px;width:364px;height:29px;background:var(--teal);color:var(--white);
  font-size:19px;font-weight:500;text-align:center;line-height:29px}
.plans-note{position:absolute;left:0;top:179px;width:364px;height:55px;background:var(--pale-box);color:var(--text-dark);
  font-size:12.3px;line-height:14.7px;text-align:center;padding-top:4px}
.plan-num{position:absolute;width:32px;height:32px;border-radius:50%;background:var(--teal);color:var(--white);
  font-size:21px;line-height:32px;text-align:center}
.plan-name{position:absolute;font-size:10.7px;color:var(--teal-text);line-height:12px}
.plan-desc{position:absolute;font-size:10.7px;color:var(--text-dark);line-height:12px}
.plan-points{position:absolute;list-style:none;font-size:10.7px;color:var(--text-dark);line-height:12.8px}
.plan-points li::before{content:"• "}
.plan-points .wrap{padding-left:8px}
.plan-points .wrap::before{content:""}
.ad-footer{position:absolute;left:0;top:650px;width:364px;height:77px;background:linear-gradient(180deg,#ececec,#e2e2e2)}
.ad-cta{position:absolute;left:28px;top:12px;width:308px;height:28px;border-radius:14px;
  background:linear-gradient(180deg,#0f6384 0%,#0a2a3a 100%);box-shadow:0 6px 6px rgba(0,0,0,.35);
  color:var(--white);font-family:"Roboto Condensed",Arial,sans-serif;font-size:16.5px;line-height:28px;text-align:center}
</style>
</head>
<body>
<section class="stage-top">
  <span class="stage-label" style="left:721px;top:60px">Banner add</span>
</section>
<section class="stage-bottom">
  <span class="stage-label" style="left:712px;top:63px">Full add</span>
</section>

<!-- Banner ad -->
<div class="banner">
  <svg class="banner-photo" width="430" height="192" role="img" aria-label="Close-up of a white keyboard with a blue Print key">
    <defs>
      <linearGradient id="keyboardTone" x1="0" y1="0" x2="1" y2="1">
        <stop offset="0" stop-color="#d9d9d9"/>
        <stop offset=".5" stop-color="#eeeeee"/>
        <stop offset="1" stop-color="#bdbdbd"/>
      </linearGradient>
    </defs>
    <path d="M0 0 H402 Q432 96 364 192 H0 Z" fill="url(#keyboardTone)"/>
  </svg>
  <div class="badge">
    <svg width="122" height="122" viewBox="-50 -50 100 100" aria-hidden="true">
      <g fill="var(--badge-navy)">
        <rect x="-38" y="-38" width="76" height="76"/>
        <rect x="-38" y="-38" width="76" height="76" transform="rotate(15)"/>
        <rect x="-38" y="-38" width="76" height="76" transform="rotate(30)"/>
        <rect x="-38" y="-38" width="76" height="76" transform="rotate(45)"/>
        <rect x="-38" y="-38" width="76" height="76" transform="rotate(60)"/>
        <rect x="-38" y="-38" width="76" height="76" transform="rotate(75)"/>
      </g>
    </svg>
    <div class="badge-text">
      <span class="badge-price">$9.95</span>
      <span class="badge-line">a month for</span>
      <span class="badge-line">3 year term</span>
    </div>
  </div>
  <h1 class="banner-title">FREE PRINTER</h1>
  <p class="banner-sub">For a monthly cost you get all<br>the supplies and service included</p>
  <div class="banner-cta">
    <span>5 PLANS AVAILABLE</span>
    <svg width="14" height="22" viewBox="0 0 14 22" aria-hidden="true"><path d="M1 1 L13 13 L8 13 L11 20 L8.5 21 L5.5 14 L1 18 Z" fill="#3f9ef5"/></svg>
  </div>
</div>

<!-- Full ad -->
<div class="full-ad">
  <div class="ad-header">
    <svg class="ad-photo" width="200" height="150" role="img" aria-label="Hand operating a grey multifunction office printer">
      <defs>
        <linearGradient id="printerTone" x1="0" y1="0" x2="1" y2="0">
          <stop offset="0" stop-color="#6c6f74"/>
          <stop offset=".6" stop-color="#a7a9ac"/>
          <stop offset="1" stop-color="#a7a9ac" stop-opacity="0"/>
        </linearGradient>
      </defs>
      <rect width="200" height="150" fill="url(#printerTone)"/>
    </svg>
    <h2 class="ad-title"><span class="free">FREE</span><span class="printer">PRINTER</span></h2>
    <div class="badge">
      <svg width="74" height="74" viewBox="-50 -50 100 100" aria-hidden="true">
        <g fill="var(--badge-navy)">
          <rect x="-38" y="-38" width="76" height="76"/>
          <rect x="-38" y="-38" width="76" height="76" transform="rotate(15)"/>
          <rect x="-38" y="-38" width="76" height="76" transform="rotate(30)"/>
          <rect x="-38" y="-38" width="76" height="76" transform="rotate(45)"/>
          <rect x="-38" y="-38" width="76" height="76" transform="rotate(60)"/>
          <rect x="-38" y="-38" width="76" height="76" transform="rotate(75)"/>
        </g>
      </svg>
      <div class="badge-text">
        <span class="badge-price">$9.95</span>
        <span class="badge-line">a month for</span>
        <span class="badge-line">3 year term</span>
      </div>
    </div>
    <p class="ad-sub">For a monthly cost you get all<br>the supplies and service included</p>
  </div>

  <div class="plans-band">5 PLANS AVAILABLE</div>
  <p class="plans-note">Prices vary upon printers, most expensive plan is<br>$69.94 a month for a 1 year term and the most affordable<br>plan is $9.95 a month for 3 year term</p>

  <div class="plan-num" style="left:22px;top:242px">1</div>
  <span class="plan-name" style="left:64px;top:245px">MONOCHROME LASER</span>
  <span class="plan-desc" style="left:64px;top:258px">(print only printer, black and white printing)</span>

  <div class="plan-num" style="left:22px;top:281px">2</div>
  <span class="plan-name" style="left:64px;top:285px">MULTIFUNCTION MONOCHROME LASER</span>
  <span class="plan-desc" style="left:64px;top:298px">(print scan copy fax printer, black and white printing)</span>
  <ul class="plan-points" style="left:64px;top:322px">
    <li>Monochrome Printers are given 1000 prints per month</li>
    <li>Toner included</li>
    <li>Service included</li>
    <li>Printer included</li>
  </ul>

  <div class="plan-num" style="left:23px;top:379px">3</div>
  <span class="plan-name" style="left:64px;top:384px">COLOR LASER</span>
  <span class="plan-desc" style="left:64px;top:397px">(print only printer, color printing)</span>

  <div class="plan-num" style="left:23px;top:424px">4</div>
  <span class="plan-name" style="left:64px;top:429px">MULTIFUNCTION COLOR LASER</span>
  <span class="plan-desc" style="left:64px;top:442px">(print scan copy fax, color printing)</span>
  <ul class="plan-points" style="left:64px;top:466px">
    <li>Color printers are given 500 monochrome prints and 500</li>
    <li class="wrap">color prints per month</li>
    <li>Toner included</li>
    <li>Service included</li>
    <li>Printer included</li>
  </ul>

  <div class="plan-num" style="left:27px;top:539px">5</div>
  <span class="plan-name" style="left:68px;top:543px">INKJET COLOR PRINTER</span>
  <span class="plan-desc" style="left:68px;top:556px">(print copy scan fax, color printing)</span>
  <ul class="plan-points" style="left:68px;top:581px">
    <li>Inkjet Printers are given 1000 prints per month.</li>
    <li>Ink included</li>
    <li>Service included</li>
    <li>Printer included</li>
  </ul>

  <div class="ad-footer">
    <div class="ad-cta">SUBSCRIPTION SERVICE FOR PRINTING</div>
  </div>
</div>
</body>
</html>
```